New business card for my lawn and landscape business

Dorrin Yard and Building is a full-service lawn care, landscaping, and light construction company serving Paragould and the Northeast Arkansas region. The business is owned and operated by Marcus Toller, with a reputation for hands-on, detail-oriented service, dependable crews, and quality results for both residential and commercial clients. A well regarded business with great reviews.
Owner Marcus Toller
Dorrinyardandbuilding.example

Target Market(s)

Commercial, Middle, and upper class in north east Arkansas

Industry/Entity Type

Lawn maintenance and landscape

Contact Information for Business Card

Dorrin Yard And Building Professional lawn care, landscaping, and property improvement in Northeast Arkansas. • lawn maintenance •lawn treatments and weed control • exterior projects • Custom landscape design & installation • Sod, trees, rock & drainage solutions • Residential & commercial services Reliable. Detailed. Done right.

Requirements
Must have
• Business name, service area, list of some of our services, clean design that represents
Nice to have
• Unique. Different design element than just grass because its already in n the logo. Picture of a warm season (south) lawn or landscape. Pictures of the type of work we do

```html
<!DOCTYPE html>
<html lang="en">
<head>
<meta charset="utf-8">
<title>Dorrin Yard and Building – Business Card</title>
<link href="https://fonts.googleapis.com/css2?family=Poppins:wght@400;500;600&display=swap" rel="stylesheet">
<style>
  :root {
    --bg: #2a2a2a;
    --card: #161616;
    --green: #7cc242;
    --white: #f2f2f2;
    --grey: #9a9a9a;
  }
  * { box-sizing: border-box; margin: 0; padding: 0; }
  html, body { width: 1200px; height: 900px; overflow: hidden; }
  body {
    background: var(--bg);
    font-family: "Poppins", sans-serif;
    position: relative;
  }
  .card {
    position: absolute;
    left: 240px;
    width: 720px;
    height: 411px;
    background: var(--card);
    border-radius: 26px;
    box-shadow: 0 10px 30px rgba(0,0,0,.45);
    overflow: hidden;
  }
  .card--front { top: 28px; }
  .card--back { top: 461px; }

  .brand {
    position: absolute;
    display: flex;
    align-items: center;
    gap: 18px;
  }
  .brand__dot {
    width: 62px; height: 62px;
    border-radius: 50%;
    background: var(--green);
    flex: none;
  }
  .brand__name {
    font-weight: 600;
    color: var(--white);
    font-size: 30px;
    line-height: 1.1;
    width: 260px;
  }
  .card--front .brand { left: 70px; top: 120px; }
  .card--back .brand { left: 60px; top: 160px; }
  .card--back .brand__name { font-size: 26px; width: 220px; }

  .holder {
    position: absolute;
    right: 60px; top: 44px;
    text-align: right;
  }
  .holder__name { color: var(--green); font-weight: 600; font-size: 27px; line-height: 1.1; }
  .holder__role { color: var(--white); font-size: 13px; }
  .holder-bar {
    position: absolute; right: 0; top: 44px;
    width: 22px; height: 34px; background: var(--green);
  }

  .contacts {
    position: absolute; left: 60px; bottom: 42px;
    list-style: none;
    color: var(--white);
    font-size: 17px;
  }
  .contacts li { display: flex; align-items: center; gap: 14px; line-height: 1.55; }
  .contacts svg { width: 16px; height: 16px; fill: var(--green); flex: none; }

  .location {
    position: absolute; right: 48px; bottom: 58px;
    border-left: 2px solid var(--green);
    padding-left: 16px;
    color: var(--white);
    font-size: 15px;
    line-height: 1.4;
  }

  .services {
    position: absolute; left: 380px; top: 70px;
    color: var(--white);
  }
  .services__title { color: var(--green); font-weight: 500; font-size: 20px; margin-bottom: 6px; }
  .services__list { list-style: none; font-size: 15px; line-height: 1.6; }
  .services__list li::before { content: "•"; color: var(--green); margin-right: 10px; }
  .services__tagline { font-size: 15px; margin-top: 2px; padding-left: 18px; }
</style>
</head>
<body>

<section class="card card--front">
  <div class="brand">
    <span class="brand__dot"></span>
    <span class="brand__name">Dorrin Yard and Building</span>
  </div>

  <div class="holder">
    <p class="holder__name">Marcus Toller</p>
    <p class="holder__role">Owner</p>
  </div>
  <span class="holder-bar"></span>

  <ul class="contacts">
    <li>
      <svg viewBox="0 0 24 24"><path d="M6.6 10.8a15 15 0 0 0 6.6 6.6l2.2-2.2a1 1 0 0 1 1-.25 11.4 11.4 0 0 0 3.6.57 1 1 0 0 1 1 1V20a1 1 0 0 1-1 1A17 17 0 0 1 3 4a1 1 0 0 1 1-1h3.5a1 1 0 0 1 1 1c0 1.25.2 2.45.57 3.6a1 1 0 0 1-.25 1z"/></svg>
      +1 870-555-0148
    </li>
    <li>
      <svg viewBox="0 0 24 24"><path d="M2 5h20v14H2z"/><path d="M2 5l10 8 10-8" fill="none" stroke="#161616" stroke-width="2"/></svg>
      Dorrinyardandbuilding@mail.example
    </li>
    <li>
      <svg viewBox="0 0 24 24"><circle cx="12" cy="12" r="10"/></svg>
      Dorrinyardandbuilding.example
    </li>
  </ul>

  <div class="location">
    <p>Brenwick, AR</p>
    <p>United States, Arkansas</p>
  </div>
</section>

<section class="card card--back">
  <div class="brand">
    <span class="brand__dot"></span>
    <span class="brand__name">Dorrin Yard and Building</span>
  </div>

  <div class="services">
    <p class="services__title">OUR SERVICES</p>
    <ul class="services__list">
      <li>Lawn maintenance</li>
      <li>Lawn treatments and weed control</li>
      <li>Exterior projects</li>
      <li>Custom landscape design &amp; installation</li>
      <li>Sod, trees, rock &amp; drainage solutions</li>
      <li>Residential &amp; commercial services</li>
    </ul>
    <p class="services__tagline">Reliable. Detailed. Done right.</p>
  </div>
</section>

</body>
</html>
```